QV Holdings Website Redesign Contest

We want to refresh our website to be more insitutional, professional for an international audience. We have designed a new logo for this purpose and that has been attached. A full brand brief and positioning statement has also been attached. Please read through all the documents carefully before designing. The old website is found here: https://qv-holdings.example/

Target Market(s)

Actuaries and associated businesses internationally

Industry/Entity Type

professional services - actuaries

Number of Pages Required

3 page

Font styles to use
Sans Serif

Colors
0054AA
0677BA
7BADD7
CADEEF
E8F1F8
0094D4
00A9DD
6FCCEA
C7EBF8
E9F6FB
F0912C
F2A743
F7CA91
FBE8D2
FDF5EE
EE7325
F08F49
F5BC92
FAE3D3
FDF4ED
EB3D1F
EC4F4E
F09395
F8D3D4
FCEDEE

Requirements
Must have
• blues and greens to match the logo color, complimentary colors, navigation
Nice to have
• old site: https://qv-holdings.example/

```html
<!DOCTYPE html>
<html lang="en">
<head>
<meta charset="utf-8">
<title>QV Holdings — Actuarial Software</title>
<link href="https://fonts.googleapis.com/css2?family=DM+Sans:wght@400;500;600;700&display=swap" rel="stylesheet">
<style>
:root{
  --navy:#0B3FA0;
  --blue:#0054AA;
  --blue-mid:#0677BA;
  --blue-soft:#CADEEF;
  --blue-pale:#E8F1F8;
  --arc:#DCE8F4;
  --orange:#EE7325;
  --orange-2:#F0912C;
  --ink:#111111;
  --text:#2b2b2b;
  --white:#ffffff;
}
*{margin:0;padding:0;box-sizing:border-box}
html,body{width:1200px;height:3819px;overflow:hidden}
body{font-family:"DM Sans",sans-serif;color:var(--text);background:var(--white);position:relative}
.abs{position:absolute}
.btn{position:absolute;display:flex;align-items:center;justify-content:center;background:var(--orange);color:var(--white);font-weight:700;text-transform:uppercase;border-radius:24px;text-decoration:none;letter-spacing:.2px}
.center{left:0;width:1200px;text-align:center}
.sec-title{position:absolute;left:0;width:1200px;text-align:center;font-size:31px;font-weight:700;color:var(--ink);letter-spacing:.3px}
.rule{position:absolute;width:34px;height:2px;background:var(--ink)}

/* header + hero */
.hero{position:absolute;left:0;top:0;width:1200px;height:960px;background:radial-gradient(ellipse at 50% 30%,#ffffff 0%,#f1f2f4 55%,#e9ebee 100%)}
.brand{position:absolute;display:flex;align-items:center;gap:12px;font-weight:600;color:var(--ink)}
.brand-dot{width:14px;height:14px;border-radius:50%;background:var(--orange)}
.login{position:absolute;left:641px;top:28px;width:123px;height:39px;border:1.5px solid var(--blue);border-radius:22px;color:var(--blue);font-size:11px;font-weight:700;display:flex;align-items:center;justify-content:center}
.nav{position:absolute;top:87px;left:559px;display:flex;font-size:13px;color:var(--ink)}
.nav a{color:var(--ink);text-decoration:none;padding:6px 11px;margin-right:4px}
.nav a.active{background:var(--blue);color:var(--white);border-radius:3px}
.hero-title{position:absolute;top:166px;font-size:40px;font-weight:700;line-height:49px;color:var(--ink)}
.hero-title span{color:var(--navy)}
.hero-sub{position:absolute;top:338px;font-size:18px;line-height:29px;color:#222}
.network{position:absolute;left:0;top:465px;width:1200px;height:490px;background:linear-gradient(90deg,rgba(240,150,120,.18),rgba(200,200,205,.25) 45%,rgba(120,180,220,.25));-webkit-mask:linear-gradient(180deg,#000 60%,transparent);mask:linear-gradient(180deg,#000 60%,transparent)}

/* platform */
.plat-title{position:absolute;left:158px;top:1013px;font-size:30px;font-weight:700;color:var(--ink)}
.plat-text{position:absolute;left:159px;top:1120px;width:320px;font-size:17px;line-height:27px;color:#222}
.diagram{position:absolute;left:494px;top:994px;width:566px;height:407px;background:radial-gradient(ellipse at 50% 50%,#e4ecf8 0%,#f3f6fb 70%);border-radius:4px}

/* core solutions */
.core{position:absolute;left:0;top:1436px;width:1200px;height:540px;background:repeating-linear-gradient(135deg,#e3ecf6 0 18px,#eaf1f8 18px 30px)}
.card{position:absolute;background:var(--white);border-radius:6px;text-align:center}
.card h3{font-size:18px;font-weight:600;color:var(--ink);line-height:22px}
.card p{font-size:13px;line-height:21px;color:#333}
.card.feature{background:var(--navy)}
.card.feature h3,.card.feature p{color:var(--white)}

/* our platform */
.step{position:absolute;width:98px;height:98px;border-radius:50%;background:var(--navy)}
.step-label{position:absolute;width:200px;text-align:center;font-size:14px;line-height:21px;color:#222}

/* articles */
.articles{position:absolute;left:0;top:2521px;width:1200px;height:653px;background:var(--blue-pale)}
.article{position:absolute;top:2699px;width:287px;height:415px;background:var(--white);border-radius:6px}
.article .thumb{position:absolute;left:12px;top:12px;width:263px;height:222px;border-radius:4px}
.article h4{position:absolute;left:25px;top:262px;width:250px;font-size:19px;font-weight:500;line-height:26px;color:var(--ink)}
.article .btn{left:25px;top:357px;width:94px;height:32px;font-size:9px}

/* cta */
.cta{position:absolute;left:0;top:3174px;width:1200px;height:308px;background:var(--navy)}

/* footer */
.foot-links{position:absolute;top:3667px;left:0;width:1200px;display:flex;justify-content:center;gap:33px;font-size:15px;color:#222}
.copy{position:absolute;top:3727px;font-size:15px;color:#222}
</style>
</head>
<body>

<section class="hero">
  <div class="brand" style="left:148px;top:36px;font-size:36px">QV Holdings<span class="brand-dot"></span></div>
  <div class="login">CLIENT LOGIN</div>
  <a class="btn" style="left:778px;top:28px;width:272px;height:39px;font-size:11px">Request a technical walkthrough</a>
  <nav class="nav">
    <a class="active">HOME</a><a>PLATFORM</a><a>SOLUTIONS</a><a>INSIGHTS</a><a>COMPANY</a><a>CONTACT</a>
  </nav>
  <h1 class="hero-title center">ACTUARIAL SOFTWARE<br>FOR STRUCTURED, AUDITABLE<br><span>FINANCIAL ANALYSIS</span></h1>
  <p class="hero-sub center">Software that translates actuarial methodologies into disciplined <b>decision-<br>ready analytical tools</b> across diverse regulatory environments.</p>
  <a class="btn" style="left:436px;top:429px;width:328px;height:47px;font-size:15px">Request a technical walkthrough</a>
  <div class="network" role="img" aria-label="Abstract network of connected nodes and lines in grey, orange and blue"></div>
</section>

<section>
  <h2 class="plat-title">PLATFORM</h2>
  <div class="rule" style="left:159px;top:1075px"></div>
  <p class="plat-text">QV Holdings develops modular actuarial software designed to support reserving, valuation, pricing, and risk analysis workflows across diverse regulatory environments.</p>
  <a class="btn" style="left:159px;top:1298px;width:169px;height:42px;font-size:12px">Explore platform</a>
  <div class="diagram" role="img" aria-label="Diagram of the modular actuarial software linking valuation, pricing, reserving, regulatory compliance, modeling engines, reporting and data input"></div>
</section>

<section class="core">
  <h2 class="sec-title" style="top:54px">CORE SOLUTIONS</h2>
  <div class="rule" style="left:583px;top:122px"></div>
</section>
<div class="card" style="left:148px;top:1619px;width:287px;height:287px">
  <svg width="72" height="80" viewBox="0 0 72 80" style="margin-top:36px" stroke="#0B3FA0" stroke-width="2.5" fill="none"><rect x="18" y="6" width="38" height="46" rx="3"/><circle cx="26" cy="20" r="7"/><path d="M34,42 v-8 M41,42 v-12 M48,42 v-16"/><path d="M4,58 h14 l14,6 h22 l12,-8 M4,58 v16 h20"/></svg>
  <h3 style="margin-top:14px">Reserving &amp; Valuation</h3>
  <p style="margin-top:16px">Software supporting structured<br>reserving workflows and financial<br>reporting across jurisdictions.</p>
</div>
<div class="card feature" style="left:457px;top:1609px;width:286px;height:306px">
  <svg width="64" height="64" viewBox="0 0 64 64" style="margin-top:38px" stroke="#fff" stroke-width="2.5" fill="none"><rect x="6" y="8" width="30" height="22" rx="2"/><path d="M10,24 l7,-7 6,5 9,-9"/><circle cx="36" cy="38" r="13"/><path d="M36,31 v14 M32,35 h6 a3,3 0 0 1 0,6 h-5"/><path d="M46,48 l10,10"/></svg>
  <h3 style="margin-top:10px">Pricing</h3>
  <p style="margin-top:16px">Models supporting insurance<br>and reinsurance pricing based on<br>actuarial methodologies.</p>
  <a class="btn" style="left:96px;top:242px;width:94px;height:32px;font-size:9px">Read more</a>
</div>
<div class="card" style="left:764px;top:1619px;width:286px;height:287px">
  <svg width="66" height="70" viewBox="0 0 66 70" style="margin-top:34px" stroke="#0B3FA0" stroke-width="2.5" fill="none"><path d="M8,4 h30 l10,10 v50 h-40z"/><text x="12" y="22" font-size="11" font-family="DM Sans, sans-serif" font-weight="700" fill="#0B3FA0" stroke="none">RISK</text><path d="M14,32 h20 M14,40 h16 M14,48 h18"/><circle cx="44" cy="46" r="11"/><path d="M52,54 l10,10"/></svg>
  <h3 style="margin-top:12px">Enterprise<br>Risk Management</h3>
  <p style="margin-top:16px">Software supporting reinsurance<br>optimization and capital<br>modeling.</p>
</div>

<section>
  <h2 class="sec-title" style="top:2036px">OUR PLATFORM</h2>
  <div class="rule" style="left:585px;top:2104px"></div>
  <svg class="abs" style="left:0;top:2160px" width="1200" height="300" viewBox="0 2160 1200 300" aria-label="Cycle of platform principles">
    <g stroke="var(--arc)" stroke-width="14" fill="none" stroke-linecap="round">
      <path d="M160,2320 A102,102 0 0 1 364,2320"/>
      <path d="M383,2310 A102,102 0 0 0 587,2310"/>
      <path d="M600,2320 A102,102 0 0 1 804,2320"/>
      <path d="M822,2310 A102,102 0 0 0 1026,2310"/>
    </g>
    <g fill="var(--arc)">
      <path d="M348,2318 h34 l-17,26z"/>
      <path d="M570,2312 h34 l-17,-26z"/>
      <path d="M788,2318 h34 l-17,26z"/>
      <path d="M1009,2312 h34 l-17,-26z"/>
    </g>
  </svg>
  <div class="step" style="left:213px;top:2254px"></div>
  <div class="step" style="left:436px;top:2275px"></div>
  <div class="step" style="left:651px;top:2254px"></div>
  <div class="step" style="left:871px;top:2275px"></div>
  <svg class="abs" style="left:0;top:2250px" width="1200" height="140" viewBox="0 2250 1200 140" stroke="#fff" stroke-width="2.2" fill="none">
    <rect x="248" y="2285" width="24" height="30" rx="2"/><path d="M253,2294 h14 M253,2301 h10"/><circle cx="271" cy="2309" r="7"/><path d="M276,2314 l6,6"/>
    <circle cx="485" cy="2324" r="19" stroke-dasharray="6 4"/><path d="M478,2318 h8 v-6 h6 v14 h-14z"/>
    <rect x="684" y="2288" width="32" height="24" rx="2"/><path d="M692,2288 v-5 h16 v5"/><circle cx="706" cy="2306" r="9"/><path d="M712,2312 l7,7"/>
    <path d="M910,2306 h18 l6,6 v26 h-24z"/><circle cx="914" cy="2325" r="9"/><path d="M907,2332 l-6,6"/>
  </svg>
  <p class="step-label" style="left:162px;top:2378px">Structured workflows<br>suitable for multi-<br>jurisdictional review</p>
  <p class="step-label" style="left:384px;top:2191px">Transparent assumptions<br>and methodological<br>clarity</p>
  <p class="step-label" style="left:600px;top:2379px">Comparative<br>scenario analysis</p>
  <p class="step-label" style="left:819px;top:2189px">Supports professional<br>judgment rather than<br>replacing it</p>
</section>

<section class="articles">
  <h2 class="sec-title" style="top:56px">LATEST ARTICLES</h2>
  <div class="rule" style="left:583px;top:123px"></div>
</section>
<article class="article" style="left:148px">
  <div class="thumb" role="img" aria-label="Magnifying glass over a dark network of connected nodes" style="background:radial-gradient(circle at 45% 45%,#6b6f78,#1a1c21 75%)"></div>
  <h4>Methodological perspectives in actuarial reserving</h4>
  <a class="btn">Read more</a>
</article>
<article class="article" style="left:457px">
  <div class="thumb" role="img" aria-label="Glowing blue magnifying glass above a digital platform" style="background:radial-gradient(circle at 50% 55%,#3aa6f0,#0a3a7a 55%,#041a3e)"></div>
  <h4>Governance considerations in multi-jurisdictional analysis</h4>
  <a class="btn">Read more</a>
</article>
<article class="article" style="left:763px">
  <div class="thumb" role="img" aria-label="Flowing wave of blue digital particles" style="background:linear-gradient(160deg,#0a1a66,#1d3fc4 55%,#081550)"></div>
  <h4>Observations on actuarial practice in emerging markets</h4>
  <a class="btn">Read more</a>
</article>

<section class="cta">
  <h2 class="abs center" style="top:82px;font-size:35px;font-weight:700;color:#fff">INTERESTED IN EXPLORING THE PLATFORM?</h2>
  <a class="btn" style="left:415px;top:169px;width:370px;height:53px;font-size:16px">Request a technical walkthrough</a>
</section>

<footer>
  <div class="brand" style="left:0;width:1200px;justify-content:center;top:3560px;font-size:50px">QV Holdings<span class="brand-dot" style="width:18px;height:18px"></span></div>
  <nav class="foot-links"><span>Company</span><span>Platform</span><span>Solutions</span><span>Insights</span><span>Contact</span></nav>
  <p class="copy center">Legal &nbsp;&nbsp;|&nbsp;&nbsp; Copyright © 2026 All Rights Reserved</p>
</footer>

</body>
</html>
```